Graphic lion print design with text

I like the gold effects in image 2 as described in my attached document, but i'm open to other suggestions. The desired image is image 1. This is a gift for a Leo friend. This is going to be printed and framed to be hung on the wall in a large frame, in landscape format. I like the idea of using different font styles to separate the statements.

Requirements
Must have
• I’m open to the suggestions about the font styles, but I want to separate the statements by using different font styles as shown in attached document.
Must be landscape format.
Small fonts preferred, as shown in the attached image.
Nice to have
• I like the gold effect in image 2 but other suggestions/colours welcome
Should not have
• Please don't stretch the picture so I can have a good resolution. Place the text on another black background template and then paste the picture beside to the text.

```html
<!DOCTYPE html>
<html lang="en">
<head>
<meta charset="utf-8">
<title>Lion Prayer Print</title>
<link rel="stylesheet" href="https://fonts.googleapis.com/css2?family=UnifrakturMaguntia&family=Josefin+Sans:wght@400&family=Arvo&family=Playball&family=Syncopate:wght@700&family=Encode+Sans+Condensed:wght@500&family=Questrial&family=Cormorant:wght@500&display=swap">
<style>
  :root {
    --page: #ffffff;
    --panel: #231f20;
    --gold-light: #f3dc8a;
    --gold: #d4aa45;
    --gold-deep: #a97c1e;
    --gold-shadow: #5a3f0c;
  }
  * { margin: 0; padding: 0; box-sizing: border-box; }
  html, body { width: 1200px; height: 1200px; overflow: hidden; background: var(--page); }
  .canvas { position: relative; width: 1200px; height: 1200px; }
  .print-panel {
    position: absolute; left: 39px; top: 195px; width: 1106px; height: 782px;
    background: var(--panel); overflow: hidden;
  }
  .lion-art {
    position: absolute; left: 580px; top: 0; width: 526px; height: 782px;
    background:
      radial-gradient(ellipse 42% 48% at 62% 50%, var(--gold) 0%, var(--gold-deep) 55%, rgba(90,63,12,0.55) 78%, rgba(35,31,32,0) 100%);
  }
  .line {
    position: absolute; white-space: nowrap; line-height: 1;
    background: linear-gradient(180deg, var(--gold-light) 0%, var(--gold) 55%, var(--gold-deep) 100%);
    -webkit-background-clip: text; background-clip: text; color: transparent;
  }
  .blackletter { font-family: "UnifrakturMaguntia", serif; }
  .thin-caps { font-family: "Josefin Sans", sans-serif; }
  .slab { font-family: "Arvo", serif; }
  .script { font-family: "Playball", cursive; }
  .wide-caps { font-family: "Syncopate", sans-serif; font-weight: 700; }
  .condensed { font-family: "Encode Sans Condensed", sans-serif; font-weight: 500; }
  .rounded { font-family: "Questrial", sans-serif; }
  .book { font-family: "Cormorant", serif; font-weight: 500; }

  .intro { left: 92px; top: 64px; font-size: 23px; }
  .headline { left: 162px; top: 110px; font-size: 48px; }
  .conqueror { left: 111px; top: 157px; font-size: 24px; letter-spacing: 0.3px; }
  .almighty { left: 112px; top: 205px; font-size: 56px; }
  .come-through { left: 91px; top: 274px; font-size: 15px; letter-spacing: 1px; }
  .seek { left: 266px; top: 288px; font-size: 29px; }
  .seek .him { font-family: "Playball", cursive; font-size: 50px; }
  .moments { left: 258px; top: 332px; font-size: 20px; }
  .calm { left: 69px; top: 376px; font-size: 20px; }
  .still { left: 178px; top: 420px; font-size: 20px; }
  .lead-word { font-size: 37px; }
  .doors { left: 86px; top: 483px; font-size: 36px; letter-spacing: 0.5px; }
  .places { left: 158px; top: 533px; font-size: 32px; }
  .waters { left: 68px; top: 605px; font-size: 27px; }
  .forsake { left: 91px; top: 638px; font-size: 27px; }
  .amen { left: 308px; top: 680px; font-size: 38px; }
</style>
</head>
<body>
<div class="canvas">
  <section class="print-panel">
    <div class="lion-art" role="img" aria-label="Gold foil illustration of a roaring lion's head in profile with splattered gold flecks"></div>

    <p class="line blackletter intro">It doesn't matter who or what may come against you,</p>
    <p class="line thin-caps headline">FOR GOD IS WITH YOU</p>
    <p class="line slab conqueror">HE has made you more than a conqueror.</p>
    <p class="line script almighty">Almighty God</p>
    <p class="line wide-caps come-through">WILL COME THROUGH FOR YOU</p>
    <p class="line condensed seek">when you seek <span class="him">Him</span></p>
    <p class="line condensed moments">in your moments of trouble and unrest.</p>
    <p class="line rounded calm"><span class="lead-word">May God</span> calm the restlessness of your mind</p>
    <p class="line rounded still"><span class="lead-word">And</span> still the thoughts that worry you.</p>
    <p class="line rounded doors">DOORS will open for you,</p>
    <p class="line blackletter places">in the most unlikeliest of places.</p>
    <p class="line book waters">When you go through deep waters, He will be with you.</p>
    <p class="line book forsake">Never will He leave you, Never will He forsake you.</p>
    <p class="line book amen">Amen.</p>
  </section>
</div>
</body>
</html>
```